New Website for QBWL Properties (Property Leasing Company in New Haven)

Design a fully functioning website for a real estate property leasing company. The company has a few properties in New Haven, CT and would like to provide an option for its tenants to pay their rent online. The company should have the ability to generate unique account log in username and password for its tenants so they can make online payments through ACH the website. (The ACH processing part will be coordinated with the bank).

Please take a look at all the pictures I uploaded of New Haven especially the area around Brindlemoor University, you will find that the general style is Gothic and charming.

Also please make use of the pictures of the two properties I have attached to the description.

Please keep Properties page, Contact Us Page , About Us Page, and please add a page entitled "Tenants".

On the Properties page I would like to see on the left hand side an interactive map of new haven (Please see a map attached), split by New Haven's neighbourhoods, and showing my properties as pins of sort on the map (I can send you the addresses of the properties upon request). On the same page on the right side I want to see a drop down menu that includes list of New Haven Neighbourhoods. When a neighbourhood is selected you can see in the space underneath the drop-down menu the properties we have in that neighbourhood in large thumbnail format. Also on the map you can see the pins corresponding to those properties change colour. A user can either click on the pin or on the thumbnails to have view more pictures of the property and some details in text.

The tenants page should prompt a login to access- I like your idea of having the company name in two colours, one for QBWL and another for Properties.Please let me know if you have any questions along the way

-------------------------------------------------------------------------------
Property Descriptions for Properties Page
The Ivory Nook,

Neighbourhood: Westville
Name: Felix Oranby House
Building Style: Queen Anne Style
Address: 514 Marrow Avenue, New Haven, CT 06592
Number of Units: 3
Unit Names: Unit 1, Unit 2, Unit 3

Property Description

This Westiville home was built in 1897, historically known as The Felix Oranby House, it is an example of the Queen Anne style. The large carriage house is still intact and sits in the lovely, expansive back garden! An outstanding architectural feature of the house is the turret, giving the home prominence on Marrow Avenue. This well maintained home has renovated kitchens in all units, the first floor has granite and red oak cabinetry. New baths and central air in all apartments. All newer mechanicals for each unit, all natural gas. The entire house has replacement windows. The new back deck overlooks the back garden and carriage house. The front steps and porch have also been rebuilt. Roof has 30 year architectural singles and approximately 15 years old, the chimney has just been lined.

Unit 1 Description:

2 Bedrooms, 6 rooms in total.
Amenities: Dishwasher, Central Air, Gas Heating, Porch

Unit 2 Description:

2 Bedrooms, 5 rooms in total.
Amenities: Dishwasher, Central Air, Gas Heating, Balcony

Unit 3 Description:

2 Bedrooms, 4 rooms in total.
Amenities: Dishwasher, Central Air, Gas Heating

The Rust Lodge:

Neighbourhood: East Rock
Name: 41 Pinfold
Building Style: Victorian
Address: 41 Pinfold Street, New Haven, CT 06598
Number of Units: 2
Unit Names: Unit 1, and Unit 2

Property Description

East Rock incredibly charming newly renovated 2 family on quiet tree-lined block. Tenants are responsible for all utilities (gas heat, electricity and cable). Small pets are possible with landlord approval. Tenants has use of shared yard, laundry in the basement and on street parking only. Located steps away from gourmet markets & minutes to Downtown New Haven, Brindlemoor & local hospitals. Fascinating backyard. This is a feel good house!

Unit 1 Description:

Area:
1100 soft, 3 Bedrooms, 5 rooms in total.
Amenities: In unit Washer and Dryer, Central Air, Gas Heating, Porch, Backyard

Unit 2 Description:

Area: 2,820 sqft
5 Bedrooms, 8 rooms in total.
Amenities: In unit Washer and Dryer, Dishwasher, Central Air, and Gas Heating

Target Market(s)

1-3 bedroom Renting Market around Brindlemoor University and New Haven Community

Industry/Entity Type

Real Estate

Coding

Coded - Design and coding required

Number of Pages Required

4 page

Font styles to use
Other font styles liked:
• Helvetica

Colors
85cae6
cee9f5
d9d9d9
9d9d9d

Requirements
Must have
• Payment page with login (accounts can only be created by administrator)
• A page showcasing the properties (Professional photos to be uploaded shortly)
• A page for technical support, contact information and so forth
• Home page
Nice to have
• A professional, but stylish design. Not too colourful, something with pastel colours
Should not have
• A lot of colours, any pop-ups,

```html
<!DOCTYPE html>
<html lang="en">
<head>
<meta charset="utf-8">
<title>QBWL Properties</title>
<link href="https://fonts.googleapis.com/css2?family=Open+Sans:wght@300;400;600;700&display=swap" rel="stylesheet">
<style>
:root{
  --blue:#3f9bd3;
  --blue-soft:#85cae6;
  --blue-pale:#cee9f5;
  --band:#4f8fbf;
  --band-dark:#3a6f98;
  --grey:#d9d9d9;
  --grey-mid:#9d9d9d;
  --light:#eeeff1;
  --ink:#333a40;
  --muted:#7d858c;
  --orange:#f5a623;
  --footer:#2c3136;
  --footer-dark:#22262a;
  --white:#fff;
}
*{box-sizing:border-box;margin:0;padding:0}
html,body{width:1200px;height:2988px;overflow:hidden}
body{font-family:"Open Sans",Helvetica,Arial,sans-serif;color:var(--ink);background:var(--white);font-size:14px}
.section{position:relative;width:1200px;overflow:hidden}
.section-title{font-size:30px;font-weight:400;letter-spacing:3px;text-transform:uppercase;color:var(--ink)}

/* top bar + nav */
.topbar{height:40px;background:var(--white);display:flex;justify-content:flex-end;align-items:center;padding:0 40px;gap:24px;font-size:12px;color:var(--muted)}
.topbar .pay-link{background:var(--blue);color:var(--white);padding:7px 16px;font-size:12px}
.nav{height:56px;display:flex;align-items:center;justify-content:space-between;padding:0 140px 0 140px;border-bottom:1px solid var(--grey)}
.brand{font-size:30px;font-weight:600;color:var(--blue)}
.brand span{color:var(--blue)}
.nav-links{display:flex;gap:0}
.nav-links a{font-size:14px;color:var(--ink);text-decoration:none;padding:18px 18px}
.nav-links a.active{color:var(--blue);border-bottom:3px solid var(--blue)}

/* hero */
.hero{height:416px;background:linear-gradient(180deg,#8da9a0 0%,#5b7560 45%,#3f5244 75%,#56624c 100%)}
.hero-arrow{position:absolute;top:180px;width:56px;height:56px;border-radius:50%;background:rgba(255,255,255,.85);display:flex;align-items:center;justify-content:center}
.hero-arrow.left{left:72px}.hero-arrow.right{right:72px}

/* find */
.find{height:328px;background:linear-gradient(180deg,#5f9cc8,#4a84b1);text-align:center;color:var(--white);padding-top:40px}
.find .section-title{color:var(--white);font-size:32px}
.find p{font-size:13px;width:760px;margin:14px auto 0;line-height:1.5;opacity:.9}
.search{width:920px;margin:30px auto 0;background:rgba(255,255,255,.22);padding:20px;display:flex;gap:20px;align-items:center}
.search-fields{flex:1;display:grid;grid-template-columns:repeat(4,1fr);gap:14px 14px}
.field{height:40px;background:var(--white);color:var(--muted);font-size:12px;text-align:left;padding:0 12px;display:flex;align-items:center;justify-content:space-between}
.field::after{content:"";border:5px solid transparent;border-top-color:var(--grey-mid);margin-top:5px}
.field.plain::after{display:none}
.search-btn{width:160px;height:94px;background:var(--orange);color:var(--white);font-weight:700;font-size:16px;display:flex;align-items:center;justify-content:center;text-align:center;line-height:1.4}

/* featured */
.featured{height:480px;padding:48px 144px 0}
.featured-head{display:flex;justify-content:space-between;align-items:center}
.featured-nav{display:flex;gap:6px}
.featured-nav span{width:36px;height:36px;background:var(--blue-soft);display:flex;align-items:center;justify-content:center}
.featured-body{display:flex;margin-top:30px;border:1px solid var(--grey)}
.featured-photo{width:500px;height:282px;background:linear-gradient(180deg,#b9d3ea 0%,#dfe7ee 55%,#6f8f4a 80%,#4e6d36 100%)}
.featured-info{flex:1;display:flex;flex-direction:column}
.info-text{flex:1;padding:22px 26px;font-size:13px;color:var(--muted);line-height:1.9}
.info-text h3{font-size:22px;font-weight:400;color:var(--ink);margin-bottom:6px}
.info-row{display:flex}.info-row b{width:130px;font-weight:400}
.info-actions{display:flex}
.info-actions a{flex:1;height:46px;display:flex;align-items:center;justify-content:center;color:var(--white);font-size:13px;font-weight:600;background:var(--blue-soft)}
.info-actions a + a{background:var(--blue)}

/* features */
.features{height:360px;background:linear-gradient(180deg,var(--band-dark),var(--band) 50%,#5c93bc);display:flex;justify-content:center;gap:190px;padding-top:100px}
.feature{text-align:center;color:var(--white);width:200px}
.feature-icon{width:100px;height:100px;border-radius:50%;background:rgba(255,255,255,.25);margin:0 auto;display:flex;align-items:center;justify-content:center;border:2px solid rgba(255,255,255,.6)}
.feature h4{margin-top:22px;font-size:14px;font-weight:700;letter-spacing:1px}

/* users */
.users{height:520px;background:var(--light);padding:52px 144px 0}
.user-grid{display:flex;gap:56px;margin-top:28px}
.user{width:200px;background:var(--white)}
.user-photo{height:200px;background:linear-gradient(180deg,#c5c9cd,#6d7680)}
.user-name{padding:10px 14px 12px;font-size:13px}
.user-name b{display:block;font-weight:700}
.user-name span{color:var(--muted);font-size:12px}
.btn-blue{display:block;width:270px;height:44px;margin:40px auto 0;background:var(--blue);color:var(--white);text-align:center;line-height:44px;font-size:14px}

/* ach */
.ach{height:120px;background:linear-gradient(90deg,#4f8dbd,#6aa6d0);display:flex;align-items:center;justify-content:center;gap:70px;color:var(--white);font-size:22px;font-weight:300}
.ach a{background:var(--orange);width:220px;height:44px;line-height:44px;text-align:center;font-size:15px;font-weight:600}

/* testimonials */
.testimonials{height:320px;text-align:center;padding-top:44px}
.dots{display:flex;justify-content:center;gap:8px;margin:18px 0 28px}
.dots i{width:8px;height:8px;border-radius:50%;background:var(--grey)}
.dots i.on{background:var(--grey-mid)}
.testimonials p{width:880px;margin:0 auto;font-size:13px;color:var(--muted);line-height:1.7}
.author{display:flex;justify-content:center;align-items:center;gap:16px;margin-top:24px;text-align:left;font-size:13px}
.author-photo{width:60px;height:60px;border-radius:50%;background:linear-gradient(180deg,#c9bdb1,#6d625a)}
.author b{display:block;font-size:15px}.author span{color:var(--muted)}

/* footer */
.footer-top{height:60px;background:var(--footer-dark);display:flex;align-items:center;justify-content:space-between;padding:0 144px}
.social{display:flex;gap:8px}
.social i{width:30px;height:30px;border:1px solid #5a6167}
.subscribe{display:flex}
.subscribe span{width:280px;height:34px;background:var(--white);color:var(--grey-mid);font-size:12px;padding:0 12px;line-height:34px}
.subscribe b{width:120px;height:34px;background:var(--blue);color:var(--white);font-size:13px;text-align:center;line-height:34px;font-weight:600}
.footer{height:220px;background:var(--footer);display:flex;padding:34px 144px 0;gap:40px;color:#aab1b7;font-size:12px;line-height:1.8}
.footer h5{color:var(--white);font-size:14px;font-weight:700;margin-bottom:12px;letter-spacing:.5px}
.col-touch{width:180px}.col-links{width:150px}.col-prop{width:310px}
.thumbs{display:grid;grid-template-columns:repeat(4,70px);gap:8px}
.thumbs i{height:54px;background:linear-gradient(180deg,#9fb3c4,#55663f)}
.map{width:170px;height:120px;background:linear-gradient(135deg,#f2e38f,#b7d48a 50%,#8fb9d9)}
.bottom{height:48px;background:var(--footer-dark);display:flex;align-items:center;justify-content:space-between;padding:0 144px;color:#8b9298;font-size:12px}
.cards{display:flex;gap:6px}.cards i{width:36px;height:22px;background:#d8dce0;border-radius:2px}
</style>
</head>
<body>

<header>
  <div class="topbar"><span>Login | Sign Up</span><span class="pay-link">Make your payment</span></div>
  <nav class="nav">
    <div class="brand">QBWL <span>Properties</span></div>
    <div class="nav-links">
      <a class="active">Home</a><a>About Us</a><a>Listing</a><a>Property</a><a>Rentals</a><a>Contact Us</a>
    </div>
  </nav>
</header>

<section class="section hero" role="img" aria-label="Photo of a Queen Anne style house with turret and porch">
  <span class="hero-arrow left"><svg width="20" height="20" viewBox="0 0 20 20"><path d="M13 3 6 10l7 7" fill="none" stroke="#555" stroke-width="3"/></svg></span>
  <span class="hero-arrow right"><svg width="20" height="20" viewBox="0 0 20 20"><path d="M7 3l7 7-7 7" fill="none" stroke="#555" stroke-width="3"/></svg></span>
</section>

<section class="section find">
  <h2 class="section-title">Find Your Place</h2>
  <p>Browse our homes across New Haven and find the apartment that fits you best. Choose the area, type and size you need, then search our current listings near Brindlemoor.</p>
  <div class="search">
    <div class="search-fields">
      <div class="field">No. Bedrooms</div><div class="field">No. Bathrooms</div><div class="field">All Areas</div><div class="field">All Type</div>
      <div class="field">No. Bathrooms</div><div class="field">No. Bedrooms</div><div class="field plain">Price</div><div class="field plain">Area</div>
    </div>
    <div class="search-btn">SEARCH<br>PROPERTY</div>
  </div>
</section>

<section class="section featured">
  <div class="featured-head">
    <h2 class="section-title">Featured Listing</h2>
    <div class="featured-nav">
      <span><svg width="12" height="12" viewBox="0 0 12 12"><path d="M8 1 3 6l5 5" fill="none" stroke="#fff" stroke-width="2"/></svg></span>
      <span><svg width="12" height="12" viewBox="0 0 12 12"><path d="M4 1l5 5-5 5" fill="none" stroke="#fff" stroke-width="2"/></svg></span>
    </div>
  </div>
  <div class="featured-body">
    <div class="featured-photo" role="img" aria-label="Photo of a modern white house with lawn"></div>
    <div class="featured-info">
      <div class="info-text">
        <h3>All information about the home</h3>
        <div>514 Marrow Avenue, New Haven, CT 06592</div>
        <div class="info-row"><b>Type:</b>Single Family</div>
        <div class="info-row"><b>Monthly Rent:</b>$ 1,800</div>
        <div class="info-row"><b>Bedrooms:</b>2</div>
        <div class="info-row"><b>Bathrooms:</b>1</div>
      </div>
      <div class="info-actions"><a>REGISTER AN INTEREST</a><a>SEE EXTERNAL HOME</a></div>
    </div>
  </div>
</section>

<section class="section features">
  <div class="feature">
    <div class="feature-icon"><svg width="44" height="44" viewBox="0 0 44 44"><path d="M6 22 22 8l16 14M11 18v18h22V18" fill="none" stroke="#fff" stroke-width="3"/></svg></div>
    <h4>HOTTEST PROPERTY LIST</h4>
  </div>
  <div class="feature">
    <div class="feature-icon"><svg width="44" height="44" viewBox="0 0 44 44"><path d="M8 8h14l16 16-14 14L8 22z" fill="none" stroke="#fff" stroke-width="3"/><circle cx="15" cy="15" r="3" fill="#fff"/></svg></div>
    <h4>BEST PRICE IN MARKET</h4>
  </div>
  <div class="feature">
    <div class="feature-icon"><svg width="44" height="44" viewBox="0 0 44 44"><path d="M22 5 36 10v12c0 9-6 14-14 17C14 36 8 31 8 22V10z" fill="none" stroke="#fff" stroke-width="3"/><path d="M15 22l5 5 9-10" fill="none" stroke="#fff" stroke-width="3"/></svg></div>
    <h4>GUARANTEED SERVICE</h4>
  </div>
</section>

<section class="section users">
  <h2 class="section-title">33 Users Are Interested In Sharing The Home</h2>
  <div class="user-grid">
    <div class="user"><div class="user-photo" role="img" aria-label="Portrait photo of a member"></div><div class="user-name"><b>Torben L.</b><span>28 Year old</span></div></div>
    <div class="user"><div class="user-photo" role="img" aria-label="Portrait photo of a member"></div><div class="user-name"><b>Marisa K.</b><span>24 Year old</span></div></div>
    <div class="user"><div class="user-photo" role="img" aria-label="Portrait photo of a member"></div><div class="user-name"><b>Corwin D.</b><span>26 Year old</span></div></div>
    <div class="user"><div class="user-photo" role="img" aria-label="Portrait photo of a member"></div><div class="user-name"><b>Helena R.</b><span>25 Year old</span></div></div>
  </div>
  <a class="btn-blue">Show all profiles</a>
</section>

<section class="section ach">
  <span>ACH processing can make online payments. then rent online</span>
  <a>Payment Now</a>
</section>

<section class="section testimonials">
  <h2 class="section-title">Clients Testimonials</h2>
  <div class="dots"><i></i><i class="on"></i><i></i></div>
  <p>Renting through this team was simple from the first visit to the signed lease. Every question was answered quickly, repairs were handled on time and paying rent online each month saves me a trip to the office. The house is warm, bright and well kept, and the neighbourhood feels like home.</p>
  <div class="author">
    <div class="author-photo" role="img" aria-label="Client portrait photo"></div>
    <div><b>Elin Marsh</b><span>Our Client</span></div>
  </div>
</section>

<footer>
  <div class="footer-top">
    <div class="social"><i></i><i></i><i></i><i></i></div>
    <div class="subscribe"><span>Enter your email</span><b>SUBSCRIBE</b></div>
  </div>
  <div class="footer">
    <div class="col-touch"><h5>GET IN TOUCH</h5>514 Marrow Avenue<br>New Haven, CT 06592<br>Tel: (203) 555-0148<br>Email: info@qbwl.com</div>
    <div class="col-links"><h5>QUICK LINKS</h5>Home<br>About Us<br>Our Rentals<br>Tenants<br>Contact Us</div>
    <div class="col-prop"><h5>OUR PROPERTY</h5>
      <div class="thumbs" role="img" aria-label="Thumbnail photos of the properties"><i></i><i></i><i></i><i></i><i></i><i></i><i></i><i></i></div>
    </div>
    <div><h5>VIEW OUR MAP</h5><div class="map" role="img" aria-label="Map of New Haven neighbourhoods"></div></div>
  </div>
  <div class="bottom"><span>© 2016 QBWL All Rights Reserved</span><div class="cards"><i></i><i></i><i></i><i></i><i></i></div></div>
</footer>

</body>
</html>
```